Landing Page für Beratungszentrum
Zielgruppe
Benötige für ein 'Kornfeld-Beratungszentrum Bau- und Immobilienökonomie' zunächst eine Landing-Page mit Einbindung 'Sachverständiger DIN EN ISO/IEC 17024 für Wertermittlung und Baukostenermittlung und -abrechnung sowie Bauablaufstörung ZERTANO 7-58-4096' sowie Link auf Hochschule (https://www.lxa-campus.de/hochschule/lehrende/ostrander-matthias/)
Nachfolgende Info gemäss Links.
https://www.kornfeld-netz.de/su/7391
https://www.kornfeld-netz.de/de/aktuelles/gruendung-kornfeld-unternehmen.html
Aufgabenstellung
Das Corporate Design von Kornfeld sollte im wesentlichen eingehalten werden. Es gibt ein Logo (beiliegend). Es gibt noch keine eigene Domain (muss noch erfunden werden www.kornfeld-bauoek.xxx; email gibt es matthias.ostrander@kfv-mail.de); rudimentäres Web/Domain Architekt gibt es (moplan.net über webtara). Bild/Bilder nach Abstimmung. Info/Leistungen muss textlich bereinigt werden.
Ein Manual Kornfeld gibt es nicht, nur einige Hinweise im Leitfaden Unternehmenskommunikation (Punkt 7.3, als PDF anbei).

```html
<!DOCTYPE html>
<html lang="de">
<head>
<meta charset="utf-8">
<title>Kornfeld-Beratungszentrum Bau- und Immobilienökonomie</title>
<link href="https://fonts.googleapis.com/css2?family=Poppins:wght@400;500;600;700&display=swap" rel="stylesheet">
<style>
:root{
  --orange:#f5a300;
  --amber:#f2ad1f;
  --amber-deep:#c98a0c;
  --ink:#111111;
  --text-gray:#555555;
  --white:#ffffff;
}
*{margin:0;padding:0;box-sizing:border-box}
html,body{width:1200px;height:3401px;overflow:hidden}
body{position:relative;font-family:'Poppins',sans-serif;color:var(--ink);background:var(--white)}
.abs{position:absolute}
.btn{position:absolute;display:flex;align-items:center;justify-content:center;font-weight:600;font-size:14px;text-decoration:none}
.btn-dark{background:var(--ink);color:var(--white)}
.btn-orange{background:var(--orange);color:var(--white)}

/* hero */
.hero{position:absolute;left:0;top:0;width:1200px;height:727px;overflow:hidden}
.hero-photo{position:absolute;inset:0;background:
  radial-gradient(ellipse 120px 260px at 1010px 420px,rgba(170,200,235,.95),rgba(170,200,235,0) 100%),
  radial-gradient(ellipse 110px 200px at 860px 440px,rgba(70,72,60,.9),rgba(70,72,60,0) 100%),
  radial-gradient(ellipse 170px 70px at 780px 540px,rgba(235,238,240,.85),rgba(235,238,240,0) 100%),
  radial-gradient(ellipse 180px 140px at 1060px 650px,rgba(40,52,75,.95),rgba(40,52,75,0) 100%),
  radial-gradient(ellipse 70px 50px at 1010px 200px,rgba(240,215,120,.9),rgba(240,215,120,0) 100%),
  radial-gradient(ellipse 320px 120px at 400px 660px,rgba(190,110,40,.55),rgba(190,110,40,0) 100%),
  radial-gradient(ellipse 260px 220px at 760px 200px,rgba(250,225,160,.55),rgba(250,225,160,0) 100%),
  linear-gradient(100deg,#f6b52a 0%,#f3ae22 35%,#e5a23a 58%,#c9914a 75%,#9a7a5c 100%)}
.brand{position:absolute;display:flex;align-items:center;gap:10px;font-weight:600;color:var(--ink)}
.brand-square{width:28px;height:28px;border:3px solid var(--ink);flex:none}
.brand-name{font-size:14px;line-height:17px}
.nav{position:absolute;left:478px;top:27px;display:flex;gap:30px;font-size:15px;font-weight:500}
.nav a{color:var(--ink);text-decoration:none}
.hero-title{left:60px;top:205px;font-size:58px;font-weight:700;line-height:70px}
.hero-sub{left:60px;top:268px;font-size:31px;font-weight:600;line-height:44px}
.hero-text{left:60px;top:368px;width:480px;font-size:14.5px;line-height:24px}

/* about */
.section-title{font-size:56px;font-weight:700;line-height:64px}
.section-sub{font-size:23px;font-weight:600;line-height:30px}
.about-title{left:80px;top:860px}
.about-sub{left:80px;top:920px;width:560px}
.about-text{left:80px;top:998px;width:560px;font-size:14.5px;line-height:24px;color:var(--text-gray)}
.about-frame{left:697px;top:817px;width:425px;height:424px;border:6px solid var(--ink);background:var(--white)}
.about-photo{position:absolute;left:21px;top:22px;width:371px;height:369px;background:
  radial-gradient(ellipse 80px 110px at 320px 170px,rgba(80,110,150,.8),rgba(80,110,150,0) 100%),
  radial-gradient(ellipse 90px 120px at 90px 200px,rgba(60,50,40,.75),rgba(60,50,40,0) 100%),
  radial-gradient(ellipse 60px 30px at 120px 50px,rgba(240,235,220,.9),rgba(240,235,220,0) 100%),
  radial-gradient(ellipse 200px 80px at 180px 340px,rgba(150,110,70,.8),rgba(150,110,70,0) 100%),
  linear-gradient(175deg,#d8b27a 0%,#c49a62 35%,#9d8264 60%,#7d6e5e 100%)}

/* services */
.services{position:absolute;left:0;top:1332px;width:1200px;height:668px;background:
  radial-gradient(ellipse 260px 200px at 200px 120px,rgba(200,140,30,.55),rgba(200,140,30,0) 100%),
  radial-gradient(ellipse 300px 220px at 1000px 200px,rgba(190,130,20,.55),rgba(190,130,20,0) 100%),
  radial-gradient(ellipse 260px 160px at 980px 560px,rgba(250,200,90,.5),rgba(250,200,90,0) 100%),
  linear-gradient(120deg,#e4a21e 0%,#f4b434 45%,#eca51c 70%,#d5951a 100%)}
.centered{left:0;width:1200px;text-align:center}
.svc-card{position:absolute;border:3px solid var(--white);box-shadow:0 4px 14px rgba(0,0,0,.25);overflow:hidden}
.svc-photo{position:absolute;inset:0}
.svc-shade{position:absolute;left:0;right:0;bottom:0;height:55%;background:linear-gradient(to bottom,rgba(0,0,0,0),rgba(0,0,0,.85))}
.svc-label{position:absolute;left:8px;bottom:10px;right:6px;color:var(--white);font-weight:600;font-size:10px;line-height:12px}
.svc-main-label{position:absolute;left:14px;right:14px;bottom:20px;color:var(--white)}
.svc-main-label h3{font-size:14px;font-weight:600;margin-bottom:4px}
.svc-main-label p{font-size:14px;line-height:21px;margin-bottom:14px}
.svc-main-label span{font-size:14px;font-weight:600}

/* case studies */
.case-card{position:absolute;overflow:hidden}
.case-label{position:absolute;left:0;right:0;bottom:14px;text-align:center;color:var(--white);font-weight:600;font-size:14px;line-height:20px}
.case-progress{left:0;top:2573px;width:1200px;height:4px;background:var(--orange)}
.case-dot{left:762px;top:2569px;width:28px;height:13px;background:var(--ink)}

/* contact */
.contact-icon{position:absolute;width:75px;height:75px;background:var(--white);box-shadow:0 2px 10px rgba(0,0,0,.15);display:flex;align-items:center;justify-content:center}
.contact-text{position:absolute;left:156px;font-size:24px;line-height:29px;letter-spacing:.3px}
.map{left:532px;top:2800px;width:609px;height:281px;background:
  radial-gradient(ellipse 230px 40px at 240px 150px,rgba(90,130,200,.75),rgba(90,130,200,0) 100%),
  radial-gradient(ellipse 120px 70px at 180px 200px,rgba(150,180,110,.7),rgba(150,180,110,0) 100%),
  radial-gradient(ellipse 90px 60px at 330px 60px,rgba(170,195,140,.7),rgba(170,195,140,0) 100%),
  radial-gradient(ellipse 140px 90px at 500px 90px,rgba(225,205,195,.7),rgba(225,205,195,0) 100%),
  linear-gradient(135deg,#e6dfca 0%,#dcd5bf 50%,#e2dbc6 100%)}

/* footer */
.footer{position:absolute;left:0;top:3170px;width:1200px;height:231px;background:var(--orange)}
.footer-brand .brand-square{width:52px;height:52px;border-width:4px}
.footer-brand .brand-name{font-size:25px;line-height:29px}
.footer-links{position:absolute;left:68px;top:146px;display:flex;gap:34px;font-size:15px}
.footer-links a{color:var(--ink);text-decoration:none}
.footer-about{position:absolute;left:840px;top:58px;width:310px;font-size:14px;line-height:18px}
.social{position:absolute;top:136px;width:29px;height:29px;border:2px solid var(--ink);border-radius:50%}
.footer-rule{position:absolute;left:60px;top:192px;width:1081px;height:2px;background:var(--ink)}
.footer-legal{position:absolute;left:0;top:205px;width:1200px;display:flex;justify-content:center;gap:30px;font-size:11px}
</style>
</head>
<body>

<header class="hero">
  <div class="hero-photo" role="img" aria-label="Zwei Bauingenieure mit Schutzhelmen und Bauplan vor einer Baustelle mit Kran im warmen Abendlicht"></div>
  <div class="brand" style="left:60px;top:22px">
    <span class="brand-square"></span>
    <span class="brand-name">Kornfeld-Beratungszentrum<br>Bau- und Immobilienökonomie</span>
  </div>
  <nav class="nav">
    <a href="#">Home</a><a href="#">About Us</a><a href="#">Services</a><a href="#">Case Studies</a>
  </nav>
  <a class="btn btn-orange" href="#" style="left:1010px;top:15px;width:137px;height:45px">Contact Us</a>
  <h1 class="abs hero-title">Expert Consulting</h1>
  <h2 class="abs hero-sub">in Construction Economics and<br>Real Estate</h2>
  <p class="abs hero-text">Rechtzeitig erkannt und gehandelt, können existenzielle Krisen vermieden oder zumindest die Schäden begrenzt werden.<br>Je früher gehandelt wird, desto größer ist der</p>
  <a class="btn btn-dark" href="#" style="left:60px;top:467px;width:138px;height:43px">Learn More</a>
</header>

<section class="about">
  <h2 class="abs section-title about-title">About Us</h2>
  <p class="abs section-sub about-sub">Building Trust with Expertise in Construction and Real Estate Economics</p>
  <p class="abs about-text">Kornfeld ist mit seiner Plattform ein verlässlic Unternehmensgründungen und Projekte. Wir unterstützen Menschen und Organisationen aus dem<br><br>akademischen und wirtschaftlichen Umfeld, die ihr Know-how durch konkrete Projekte in Forschungn.</p>
  <a class="btn btn-orange" href="#" style="left:80px;top:1145px;width:136px;height:45px">Learn More</a>
  <div class="abs about-frame">
    <div class="about-photo" role="img" aria-label="Bauingenieure mit Helmen besprechen Pläne auf einer Baustelle bei Sonnenuntergang"></div>
  </div>
</section>

<section class="services" role="img" aria-label="Hintergrundfoto eines Beratungsgesprächs in warmem Orangeton">
  <h2 class="abs section-title centered" style="top:40px">Services</h2>
  <p class="abs section-sub centered" style="top:100px">Building Strong Foundations with Expert Construction Services</p>

  <div class="svc-card" style="left:60px;top:272px;width:130px;height:180px">
    <div class="svc-photo" role="img" aria-label="Hände über Dokumenten bei einer Wertermittlung" style="background:radial-gradient(ellipse 50px 40px at 70px 70px,rgba(215,170,140,.85),rgba(215,170,140,0) 100%),radial-gradient(ellipse 60px 30px at 50px 120px,rgba(30,30,35,.8),rgba(30,30,35,0) 100%),linear-gradient(160deg,#f2f2f2,#cfcfcf 60%,#8a8a8a)"></div>
    <div class="svc-shade"></div><div class="svc-label">Valuation Services</div>
  </div>
  <div class="svc-card" style="left:214px;top:233px;width:186px;height:258px">
    <div class="svc-photo" role="img" aria-label="Geschäftsmann vor Finanzdiagrammen" style="background:radial-gradient(ellipse 70px 110px at 70px 90px,rgba(30,35,45,.9),rgba(30,35,45,0) 100%),radial-gradient(ellipse 90px 50px at 110px 170px,rgba(60,110,170,.85),rgba(60,110,170,0) 100%),linear-gradient(160deg,#e6e8ea,#b8c2cc 50%,#4d5d6e)"></div>
    <div class="svc-shade"></div><div class="svc-label">Financial And<br>Economic Analysis</div>
  </div>
  <div class="svc-card" style="left:423px;top:176px;width:355px;height:370px">
    <div class="svc-photo" role="img" aria-label="Person in blauer Kleidung arbeitet an einem Tablet" style="background:radial-gradient(ellipse 120px 70px at 150px 120px,rgba(225,228,232,.95),rgba(225,228,232,0) 100%),radial-gradient(ellipse 140px 160px at 270px 110px,rgba(70,130,190,.9),rgba(70,130,190,0) 100%),radial-gradient(ellipse 90px 120px at 60px 80px,rgba(90,150,200,.8),rgba(90,150,200,0) 100%),linear-gradient(160deg,#8fb3d6,#5f8fbf 55%,#2f3d4d)"></div>
    <div class="svc-shade" style="height:60%"></div>
    <div class="svc-main-label">
      <h3>COST DETERMINATION AND BILLING</h3>
      <p>Kornfeld ist mit seiner Plattform verlässlic Unternehmensgründungen und</p>
      <span>Learn More</span>
    </div>
  </div>
  <div class="svc-card" style="left:802px;top:233px;width:186px;height:258px">
    <div class="svc-photo" role="img" aria-label="Zwei Ingenieure auf einer Baustelle mit Gerüst" style="background:radial-gradient(ellipse 30px 60px at 75px 130px,rgba(190,220,60,.85),rgba(190,220,60,0) 100%),radial-gradient(ellipse 40px 70px at 125px 130px,rgba(90,120,170,.85),rgba(90,120,170,0) 100%),radial-gradient(ellipse 90px 60px at 100px 60px,rgba(200,150,90,.7),rgba(200,150,90,0) 100%),linear-gradient(180deg,#e6eaee,#cdbfa8 45%,#7d6d5a)"></div>
    <div class="svc-shade"></div><div class="svc-label">CONSTRUCTION PROCESS<br>OPTIMIZATION</div>
  </div>
  <div class="svc-card" style="left:1012px;top:272px;width:130px;height:180px">
    <div class="svc-photo" role="img" aria-label="Dozent vor einer Tafel in einem Seminarraum" style="background:radial-gradient(ellipse 30px 60px at 65px 90px,rgba(190,210,225,.9),rgba(190,210,225,0) 100%),radial-gradient(ellipse 25px 40px at 65px 145px,rgba(60,70,90,.8),rgba(60,70,90,0) 100%),linear-gradient(160deg,#f4f4f2,#dcdcd8 55%,#9a9c9f)"></div>
    <div class="svc-shade"></div><div class="svc-label">Academic And<br>Professional Training</div>
  </div>

  <a class="btn btn-dark" href="#" style="left:520px;top:574px;width:161px;height:43px">Discover More</a>
</section>

<section class="cases">
  <h2 class="abs section-title centered" style="top:2081px">Case Studies</h2>
  <p class="abs section-sub centered" style="top:2142px">Delivering Results: Case Studies That Speak for Themselves</p>

  <div class="case-card" style="left:0;top:2288px;width:252px;height:197px">
    <div class="svc-photo" role="img" aria-label="Hände zeigen auf Diagramme auf einem Tablet" style="background:radial-gradient(ellipse 80px 50px at 140px 80px,rgba(40,45,55,.85),rgba(40,45,55,0) 100%),radial-gradient(ellipse 60px 40px at 70px 60px,rgba(205,165,135,.8),rgba(205,165,135,0) 100%),linear-gradient(160deg,#f0f2f4,#c8d0d8 55%,#6a7686)"></div>
    <div class="svc-shade"></div><div class="case-label">SOFTWARE<br>DEVELOPMENT</div>
  </div>
  <div class="case-card" style="left:262px;top:2288px;width:258px;height:197px">
    <div class="svc-photo" role="img" aria-label="Zwei Personen vor einem Bildschirm mit Kursdiagrammen" style="background:radial-gradient(ellipse 110px 80px at 180px 80px,rgba(120,200,200,.85),rgba(120,200,200,0) 100%),radial-gradient(ellipse 60px 90px at 60px 90px,rgba(30,35,40,.85),rgba(30,35,40,0) 100%),linear-gradient(160deg,#5f8c96,#2f4750 70%,#1c2a30)"></div>
    <div class="svc-shade"></div><div class="case-label">IT SUPPORT AND<br>MAINTENANCE</div>
  </div>
  <div class="case-card" style="left:530px;top:2231px;width:409px;height:310px;box-shadow:0 6px 18px rgba(0,0,0,.3)">
    <div class="svc-photo" role="img" aria-label="Person in blauer Kleidung rechnet mit Taschenrechner am Schreibtisch" style="background:radial-gradient(ellipse 160px 110px at 240px 90px,rgba(80,150,210,.95),rgba(80,150,210,0) 100%),radial-gradient(ellipse 70px 90px at 60px 70px,rgba(120,60,50,.75),rgba(120,60,50,0) 100%),radial-gradient(ellipse 80px 40px at 160px 190px,rgba(235,230,225,.85),rgba(235,230,225,0) 100%),linear-gradient(170deg,#6d8db5,#7fa4cc 45%,#3a3d42)"></div>
    <div class="svc-shade" style="height:45%"></div>
    <div class="case-label" style="font-size:17px;line-height:26px;bottom:20px">DATA ANALYTICS AND BUSINESS<br>INTELLIGENCE</div>
  </div>
  <div class="case-card" style="left:949px;top:2288px;width:251px;height:197px">
    <div class="svc-photo" role="img" aria-label="Gruppe von Menschen schaut gemeinsam auf ein Dokument" style="background:radial-gradient(ellipse 60px 60px at 60px 60px,rgba(150,100,75,.8),rgba(150,100,75,0) 100%),radial-gradient(ellipse 60px 60px at 170px 60px,rgba(150,100,75,.75),rgba(150,100,75,0) 100%),radial-gradient(ellipse 120px 60px at 120px 140px,rgba(60,100,160,.9),rgba(60,100,160,0) 100%),linear-gradient(160deg,#5c7590,#2e3b4a)"></div>
    <div class="svc-shade"></div><div class="case-label">NETWORK<br>INFRASTRUCTURE</div>
  </div>
  <div class="abs case-progress"></div>
  <div class="abs case-dot"></div>
</section>

<section class="contact">
  <h2 class="abs section-title centered" style="top:2662px">Contact Us</h2>
  <p class="abs section-sub centered" style="top:2724px">Get in Touch, We’re Here to Help</p>

  <div class="contact-icon" style="left:60px;top:2800px">
    <svg width="40" height="28" viewBox="0 0 40 28"><rect width="40" height="28" rx="2" fill="#f5a300"/><path d="M2 3 L20 16 L38 3" fill="none" stroke="#fff" stroke-width="2.5"/><path d="M2 26 L15 13 M38 26 L25 13" stroke="#fff" stroke-width="2"/></svg>
  </div>
  <p class="contact-text" style="top:2823px">lena.brandt@example.com</p>

  <div class="contact-icon" style="left:60px;top:2902px">
    <svg width="38" height="38" viewBox="0 0 24 24"><path fill="#f5a300" d="M6.6 10.8a15.1 15.1 0 0 0 6.6 6.6l2.2-2.2c.3-.3.7-.4 1-.2 1.1.4 2.3.6 3.6.6.6 0 1 .4 1 1V20c0 .6-.4 1-1 1A17 17 0 0 1 3 4c0-.6.4-1 1-1h3.5c.6 0 1 .4 1 1 0 1.3.2 2.5.6 3.6.1.3 0 .7-.2 1z"/></svg>
  </div>
  <p class="contact-text" style="top:2925px">(270) 555-0184</p>

  <div class="contact-icon" style="left:60px;top:3005px">
    <svg width="30" height="40" viewBox="0 0 30 40"><path fill="#f5a300" d="M15 0C6.7 0 0 6.7 0 15c0 11 15 25 15 25s15-14 15-25C30 6.7 23.3 0 15 0z"/><circle cx="15" cy="15" r="6" fill="#fff"/></svg>
  </div>
  <p class="contact-text" style="top:3013px">4307 Birchwood Ln. Hartwell<br>Connecticut 35618</p>

  <div class="abs map" role="img" aria-label="Stadtplan mit Flusslauf und Standortmarkierung des Büros"></div>
</section>

<footer class="footer">
  <div class="brand footer-brand" style="left:60px;top:54px">
    <span class="brand-square"></span>
    <span class="brand-name">Kornfeld-Beratungszentrum<br>Bau- und Immobilienökonomie</span>
  </div>
  <p class="footer-about">Lorem Ipsum Dolor Sit Amet Consectetur. Aliquam Dolor Consequat Eu Ac Mus Orci Amet Erat Molestie Vitae.</p>
  <nav class="footer-links">
    <a href="#">Home</a><a href="#">About Us</a><a href="#">Services</a><a href="#">Case Studies</a>
  </nav>
  <span class="social" style="left:840px"></span>
  <span class="social" style="left:885px"></span>
  <span class="social" style="left:929px"></span>
  <span class="social" style="left:974px"></span>
  <div class="footer-rule"></div>
  <div class="footer-legal">
    <span>Copyright © 2024 All Right Reserved</span><span>Privacy Policy</span><span>Terms Of Service</span><span>Cookies Settings</span>
  </div>
</footer>

</body>
</html>
```